Brellify Sponsored Content Images

Image spec: 1.91:1 ratio (1200x627px)We require 6x variations of this image: See the excel attached for the copy.Each image should contain the OSKEL logo, 2 headshots if posible, a designed background and a CTA button + the copy.Please make sure that all of the copy is clear and big enough to read so it can be read on mobile devices.

Target Market(s)

This is for Brellify ads to Executives of mid-market companies

Font styles to use
Sans Serif

Colors

Designer to choose colors to be used in the design.

```html
<!DOCTYPE html>
<html lang="en">
<head>
<meta charset="utf-8">
<title>OSKEL Ad-1</title>
<link rel="stylesheet" href="https://fonts.googleapis.com/css2?family=Poppins:ital,wght@0,400;0,500;0,700;1,600&display=swap">
<style>
  :root {
    --board-light: #e2e2e2;
    --board-dark: #d9d9d9;
    --label: #1a1a1a;
    --navy-deep: #020b3a;
    --navy: #06247a;
    --blue-glow: #1e6fe0;
    --cyan: #34c8ff;
    --white: #ffffff;
    --yellow: #f7e21b;
    --ink: #0b1d5c;
  }
  * { margin: 0; padding: 0; box-sizing: border-box; }
  html, body { width: 1200px; height: 742px; overflow: hidden; }
  body {
    position: relative;
    background: var(--board-dark);
    font-family: "Poppins", sans-serif;
  }
  .board-shade { position: absolute; inset: 0; width: 1200px; height: 742px; }
  .board-label {
    position: absolute; top: 138px; left: 0; width: 1200px;
    text-align: center; font-size: 13px; color: var(--label);
  }
  .ad {
    position: absolute; left: 233px; top: 182px; width: 720px; height: 376px;
    overflow: hidden;
    background:
      radial-gradient(ellipse 260px 200px at 210px 120px, rgba(40,90,200,.45), transparent 70%),
      linear-gradient(160deg, var(--navy-deep) 0%, #031a5c 55%, var(--navy) 100%);
  }
  .network-art {
    position: absolute; right: 0; top: 0; width: 330px; height: 376px;
    background:
      radial-gradient(circle at 200px 150px, rgba(52,200,255,.28), transparent 55%),
      radial-gradient(circle at 260px 240px, rgba(30,111,224,.35), transparent 60%),
      linear-gradient(90deg, transparent, rgba(30,111,224,.18));
  }
  .brand {
    position: absolute; left: 606px; top: 24px;
    display: flex; align-items: center; gap: 6px;
    color: var(--white); font-weight: 500; font-size: 26px; letter-spacing: .5px;
  }
  .brand-mark { width: 10px; height: 10px; background: var(--white); }
  .headshot {
    position: absolute; top: 41px; width: 114px; height: 95px;
    border-radius: 50px 50px 6px 6px;
    background: linear-gradient(180deg, #8a6a55 0%, #c89a80 45%, #9fc0e6 80%, #e9eef6 100%);
    opacity: .9;
  }
  .headshot.left { left: 60px; }
  .headshot.right { left: 232px; background: linear-gradient(180deg, #6b5240 0%, #d6a888 45%, #f2f2f2 80%, #ffffff 100%); }
  .copy { position: absolute; left: 0; top: 158px; width: 420px; text-align: center; }
  .eyebrow { color: var(--white); font-weight: 700; font-size: 21px; line-height: 28px; }
  .headline { color: var(--yellow); font-weight: 700; font-size: 22px; line-height: 28px; }
  .subline { color: var(--white); font-size: 15.5px; line-height: 24px; margin-top: -1px; }
  .subline em { font-weight: 600; font-style: italic; }
  .date-ribbon {
    position: absolute; left: 73px; top: 247px; width: 274px; height: 34px;
    background: var(--white);
    clip-path: polygon(0 0, 100% 0, 97% 50%, 100% 100%, 0 100%, 3% 50%);
    color: var(--ink); font-style: italic; font-weight: 600; font-size: 15px;
    display: flex; align-items: center; justify-content: center;
  }
  .cta {
    position: absolute; left: 120px; top: 294px; width: 180px; height: 34px;
    background: var(--yellow); border-radius: 9px;
    color: var(--ink); font-weight: 500; font-size: 16.5px;
    display: flex; align-items: center; justify-content: center;
  }
</style>
</head>
<body>
  <svg class="board-shade" viewBox="0 0 1200 742" aria-hidden="true">
    <polygon points="0,0 1200,0 1200,463 0,321" fill="var(--board-light)"/>
  </svg>
  <p class="board-label">OSKEL Ad-1</p>

  <section class="ad">
    <div class="network-art" role="img" aria-label="Glowing blue circuit network of hexagons with padlock icons"></div>
    <div class="brand"><span class="brand-mark"></span>OSKEL</div>

    <div class="headshot left" role="img" aria-label="Headshot of the first webinar speaker"></div>
    <div class="headshot right" role="img" aria-label="Headshot of the second webinar speaker"></div>

    <div class="copy">
      <p class="eyebrow">Free Live Webinar:</p>
      <h1 class="headline">Cybersecurity Starts at the Top</h1>
      <p class="subline">How to <em>'Sell'</em> a cybersecurity strategy internally</p>
    </div>

    <div class="date-ribbon">Wednesday, June 12th at 1pm EST</div>
    <div class="cta">Book your place</div>
  </section>
</body>
</html>
```